KVT Business Cards

We require business cards for our business. We would like a matte black back to the card, with our logo centred in the middle. The front side of the card is open to design.

Target Market(s)

Clients looking for legal services (professional)

Industry/Entity Type

Legal

Contact Information for Business Card

Boris Telemark
Partner
Mobile: 0438 715 642
Email: boris@kvtlaw.co
Website: www.kvtlaw.co
Level 3, 118 Wexbury Street
Sydney NSW 2000

Font styles to use
Other font styles liked:
• Avenir

Colors
f04a50
ffffff
1b1b1b

Requirements
Must have
• Black back with logo included in the centre of the card.
• Our font is Avenir.

```html
<!DOCTYPE html>
<html lang="en">
<head>
<meta charset="utf-8">
<title>KVT Legal – Business Cards</title>
<link rel="stylesheet" href="https://fonts.googleapis.com/css2?family=Montserrat:wght@400;500;600;700&display=swap">
<style>
  :root {
    --page: #1b1b1b;
    --card-front: #ebebeb;
    --card-back: #0f0f0f;
    --ink: #1b1b1b;
    --accent: #c0203e;
    --back-mark: #262626;
  }
  * { margin: 0; padding: 0; box-sizing: border-box; }
  html, body {
    width: 1200px; height: 1200px; overflow: hidden;
    background: var(--page);
    font-family: "Montserrat", sans-serif;
  }
  .canvas { position: relative; width: 1200px; height: 1200px; }
  .card { position: absolute; left: 227px; width: 746px; height: 426px; }
  .card--front { top: 135px; background: var(--card-front); color: var(--ink); }
  .card--back { top: 639px; background: var(--card-back); }

  .brand { position: absolute; display: flex; align-items: center; gap: 18px; }
  .brand__square { width: 30px; height: 30px; background: var(--accent); }
  .brand__name { font-weight: 700; font-size: 44px; letter-spacing: 0.5px; line-height: 1; }
  .card--front .brand { right: 36px; top: 90px; }
  .card--front .brand__name { color: var(--ink); }
  .card--back .brand { left: 50%; top: 50%; transform: translate(-50%, -50%); }
  .card--back .brand__square { background: var(--back-mark); }
  .card--back .brand__name { color: var(--back-mark); }

  .holder { position: absolute; left: 36px; top: 236px; }
  .holder__name { color: var(--accent); font-weight: 600; font-size: 23px; letter-spacing: 0.6px; }
  .holder__role { font-size: 17px; margin-top: 4px; }

  .divider { position: absolute; left: 0; right: 0; top: 302px; height: 1px; background: var(--ink); }
  .divider__accent {
    position: absolute; left: 36px; top: 300px; width: 178px; height: 0;
    border-top: 2px dotted var(--accent); background: var(--card-front);
  }
  .divider__gap { position: absolute; left: 34px; top: 301px; width: 182px; height: 3px; background: var(--card-front); }

  .contacts { position: absolute; left: 36px; top: 322px; list-style: none; font-size: 17px; }
  .contacts li { display: flex; align-items: center; gap: 9px; height: 24px; }
  .contacts svg { width: 17px; height: 17px; flex: none; }
  .contacts .highlight { color: var(--accent); }

  .address { position: absolute; right: 34px; top: 346px; text-align: right; font-size: 17px; line-height: 24px; }
</style>
</head>
<body>
<main class="canvas">
  <section class="card card--front">
    <div class="brand">
      <span class="brand__square"></span>
      <span class="brand__name">KVT LEGAL</span>
    </div>

    <div class="holder">
      <p class="holder__name">Boris Telemark</p>
      <p class="holder__role">Partner</p>
    </div>

    <div class="divider"></div>
    <div class="divider__gap"></div>
    <div class="divider__accent"></div>

    <ul class="contacts">
      <li>
        <svg viewBox="0 0 20 20" aria-hidden="true"><circle cx="10" cy="10" r="10" fill="#c0203e"/><path d="M5 8c0-2 2-3 5-3s5 1 5 3l-2 1-1-2H8L7 9z M6 14l2-4h4l2 4z" fill="#fff"/></svg>
        <span>0438 715 642</span>
      </li>
      <li>
        <svg viewBox="0 0 20 20" aria-hidden="true"><circle cx="10" cy="10" r="10" fill="#c0203e"/><rect x="5" y="6.5" width="10" height="7" fill="none" stroke="#fff" stroke-width="1.3"/><path d="M5 6.5l5 4 5-4" fill="none" stroke="#fff" stroke-width="1.3"/></svg>
        <span>boris@kvtlaw.co</span>
      </li>
      <li>
        <svg viewBox="0 0 20 20" aria-hidden="true"><circle cx="10" cy="10" r="10" fill="#c0203e"/><circle cx="10" cy="10" r="5.5" fill="none" stroke="#fff" stroke-width="1.3"/><path d="M4.5 10h11M10 4.5c-2.5 3-2.5 8 0 11M10 4.5c2.5 3 2.5 8 0 11" fill="none" stroke="#fff" stroke-width="1.1"/></svg>
        <span>www.<span class="highlight">kvtlaw</span>.co</span>
      </li>
    </ul>

    <address class="address" style="font-style:normal">
      Level 3, 118 Wexbury Street<br>
      Sydney NSW 2000
    </address>
  </section>

  <section class="card card--back">
    <div class="brand">
      <span class="brand__square"></span>
      <span class="brand__name">KVT LEGAL</span>
    </div>
  </section>
</main>
</body>
</html>
```